Aufkleberdesign für 3d Messdienstleistungen
Zielgruppe
3d Messdienstleistungen in Industrie, Architektur und Schiffbau
Aufgabenstellung
technisches Design, ansprechend, rational
Wir benötigen Aufkleber mit sehr kurzen Informationen über unsere Dienstleistung, die wir auf den Messobjekten bei unseren Kunden hinterlassen,
- Logo (vorhanden),
- Kontaktdaten,
- Dienstleistungen (Liste von 4-5 Schlagwörtern), (Kalibrierung von Laserprojektion, Industrievermessung, Kranbahnvermessung, Bauwerksvermessung)
- netter Hintergrund
A4, A5, A6 für Druck, Querformat

```html
<!DOCTYPE html>
<html lang="de">
<head>
<meta charset="utf-8">
<title>Nordmaß 3D Systeme – Aufkleber</title>
<link href="https://fonts.googleapis.com/css2?family=Montserrat:wght@300;600&display=swap" rel="stylesheet">
<style>
  :root {
    --bg: #000000;
    --accent: #1a9be0;
    --text: #ffffff;
    --wire: #1f6f9a;
    --wire-deep: #0a2c40;
  }
  * { margin: 0; padding: 0; box-sizing: border-box; }
  html, body { width: 1200px; height: 849px; overflow: hidden; background: var(--bg); }
  .sticker {
    position: relative;
    width: 1200px;
    height: 849px;
    background: var(--bg);
    font-family: "Montserrat", sans-serif;
    color: var(--text);
    overflow: hidden;
  }
  .building-visual {
    position: absolute;
    left: 430px;
    top: 180px;
    width: 770px;
    height: 669px;
  }
  .brand {
    position: absolute;
    left: 76px;
    top: 120px;
    display: flex;
    align-items: center;
    gap: 18px;
  }
  .brand-mark {
    width: 54px;
    height: 54px;
    background: var(--accent);
  }
  .brand-name {
    font-weight: 300;
    font-size: 34px;
    letter-spacing: 10px;
    color: var(--text);
  }
  .section-title {
    position: absolute;
    left: 58px;
    font-weight: 600;
    font-size: 42px;
    color: var(--accent);
    line-height: 1;
  }
  .section-title.contact { top: 372px; }
  .section-title.services { top: 592px; }
  .info-list {
    position: absolute;
    left: 58px;
    list-style: none;
    font-weight: 600;
    font-size: 29px;
    line-height: 37.7px;
  }
  .info-list.contact { top: 414px; }
  .info-list.services { top: 634px; }
</style>
</head>
<body>
<div class="sticker">
  <svg class="building-visual" role="img" aria-label="Blaue Drahtgitter-Darstellung eines Gebäudeinnenraums in Perspektive" viewBox="0 0 770 669" preserveAspectRatio="none">
    <defs>
      <radialGradient id="wireGlow" cx="0.6" cy="0.55" r="0.6">
        <stop offset="0" stop-color="var(--wire)" stop-opacity="0.55"/>
        <stop offset="0.55" stop-color="var(--wire-deep)" stop-opacity="0.45"/>
        <stop offset="1" stop-color="#000000" stop-opacity="0"/>
      </radialGradient>
    </defs>
    <rect width="770" height="669" fill="url(#wireGlow)"/>
  </svg>

  <div class="brand">
    <span class="brand-mark"></span>
    <span class="brand-name">NORDMASS 3D</span>
  </div>

  <h2 class="section-title contact">Kontakt</h2>
  <ul class="info-list contact">
    <li>Nordmaß 3D Systeme GmbH</li>
    <li>Phone : +49 (0)4100 5550123</li>
    <li>E-Mail&nbsp; : info@nordmass-3d.de</li>
  </ul>

  <h2 class="section-title services">Services</h2>
  <ul class="info-list services">
    <li>- Kalibrierung von Laserprojektion</li>
    <li>- Industrievermessung</li>
    <li>- Kranbahnvermessung</li>
    <li>- Bauwerksvermessung</li>
  </ul>
</div>
</body>
</html>
```